FREE SOCIAL SECURITY DISABILITY CLAIM EVALUATION - Ad Banners & Email Marketing Creatives

Looking for design of ad banners and email creative for my Social Security Disability Insurance Benefits Application, Denial, & Appeals Help website. Call to action based email focused on conveying brand, messaging of "Are you out of work due to a disability? You may qualify for up to $2,642 per month in Social Security Disability benefits!" and "ACT NOW: Check Your Eligibility" Call to action of 'Get Your FREE Evaluation' or 'Fast, FREE, No Obligation Evaluation' or 'Confirm My Eligibility Now!' or 'Start My FREE Evaluation' or 'Confirm My Eligibility Now!'. Can use any messaging and images from the current website:
https://relief-filingdesk.com/

Please focus on imaging that matches the site. The final Ad Banners must be delivered in both JPG and PSD file formats. Ad Banners must follow OMC standards.

We need Ad Banners in the following sizes.
728x90
300x250
336x280
160x600
1200x628
600x600
1080x1080
Email

Target Market(s)
People in the US between the ages 48-63 looking for Social Security Disability Insurance Benefits Application, Denial, & Appeals Help. Get connected to a local Social Security Disability legal representative for a free, no-obligation evaluation. Find out if you are eligible to receive financial compensation for as much as $2,642 a month!

Should not be cookie cutter. Stick to simple yet official looking.

The final Email creative must be done in responsive HTML as well as text for easy use and include Email Opt Out link etc.

Target Market(s)

Americans that are between the ages 48-63 that have a physical condition that prevents them from working. Many times the physical condition is a result of an injury.

Coding

Coded - Design and coding required

Font styles to use
Sans Serif

Requirements
Must have
• A strong call to action.
Should not have
• No photos of people in wheelchairs.

```html
<!DOCTYPE html>
<html lang="en">
<head>
<meta charset="utf-8">
<title>Free Social Security Disability Claim Evaluation – Ad Banners</title>
<link rel="stylesheet" href="https://fonts.googleapis.com/css2?family=IBM+Plex+Sans:wght@400;500;700&family=Oswald:wght@400&display=swap">
<style>
  :root {
    --navy-deep: #0c1a3f;
    --navy: #172e5e;
    --navy-mid: #2a4a80;
    --steel: #3f5f9b;
    --orange: #e09b2d;
    --white: #ffffff;
    --board: #c5c5c5;
    --ring: #dedede;
    --seal: #8cc2e4;
    --photo-warm: #b9a48e;
    --photo-cool: #9ea6ae;
  }
  * { box-sizing: border-box; margin: 0; padding: 0; }
  html, body { width: 1200px; height: 1179px; overflow: hidden; }
  body {
    font-family: "IBM Plex Sans", Arial, sans-serif;
    color: var(--white);
    background: var(--board);
    position: relative;
  }
  .board-shapes { position: absolute; inset: 0; }

  .banner {
    position: absolute;
    overflow: hidden;
    box-shadow: 0 14px 36px rgba(0,0,0,.35);
  }
  .brand-row { position: absolute; display: flex; align-items: center; z-index: 2; }
  .brand-mark { background: var(--seal); flex: none; }
  .brand-name {
    font-family: "Oswald", "Arial Narrow", sans-serif;
    font-weight: 400;
    letter-spacing: .08em;
    text-transform: uppercase;
    white-space: nowrap;
    line-height: 1;
  }
  .headline { position: absolute; font-weight: 700; line-height: 1.3; }
  .subline { position: absolute; font-weight: 500; line-height: 1.3; }
  .act-now { position: absolute; font-weight: 700; color: var(--orange); letter-spacing: .01em; }
  .check { position: absolute; font-weight: 700; }
  .cta {
    position: absolute;
    background: var(--orange);
    border-radius: 999px;
    font-weight: 700;
    text-transform: uppercase;
    display: flex; align-items: center; justify-content: center;
    white-space: nowrap;
  }

  /* Landscape banner */
  .banner-wide {
    left: 58px; top: 73px; width: 706px; height: 369px;
    background: linear-gradient(180deg, var(--navy-deep) 0%, var(--navy) 45%, var(--navy-mid) 100%);
  }
  .banner-wide .brand-row { left: 32px; top: 19px; }
  .banner-wide .brand-mark { width: 41px; height: 37px; }
  .banner-wide .brand-name { font-size: 12px; margin-left: 6px; }
  .banner-wide .headline { left: 32px; top: 70px; font-size: 25px; }
  .banner-wide .subline { left: 32px; top: 146px; font-size: 15.5px; line-height: 1.27; }
  .banner-wide .act-now { left: 32px; top: 222px; font-size: 31px; }
  .banner-wide .check { left: 32px; top: 268px; font-size: 19px; }
  .banner-wide .cta { left: 32px; top: 313px; width: 197px; height: 37px; font-size: 10.5px; }
  .banner-wide .photo-ring { position: absolute; left: 0; top: 0; }

  /* Square banner */
  .banner-square {
    left: 789px; top: 73px; width: 353px; height: 353px;
    background: linear-gradient(135deg, #34548e 0%, var(--steel) 55%, #4c6aa3 100%);
  }
  .banner-square .photo-fill { position: absolute; inset: 0; background: radial-gradient(circle at 78% 28%, rgba(150,170,210,.45), rgba(60,90,150,0) 55%); }
  .banner-square .brand-row { left: 17px; top: 32px; }
  .banner-square .brand-mark { width: 22px; height: 19px; }
  .banner-square .brand-name { font-size: 6.8px; margin-left: 3px; letter-spacing: .06em; }
  .banner-square .headline { left: 17px; top: 64px; font-size: 22px; line-height: 1.25; }
  .banner-square .subline { left: 17px; top: 130px; font-size: 12.5px; line-height: 1.45; }
  .banner-square .act-now { left: 17px; top: 185px; font-size: 32px; }
  .banner-square .check { left: 17px; top: 232px; font-size: 20px; }
  .banner-square .cta { left: 18px; top: 282px; width: 293px; height: 39px; font-size: 11px; }

  /* Tall square banner */
  .banner-feature {
    left: 58px; top: 471px; width: 635px; height: 635px;
    background: linear-gradient(180deg, var(--navy-deep) 0%, var(--navy) 50%, #1f3b70 100%);
    text-align: center;
  }
  .banner-feature .brand-row { left: 117px; top: 29px; }
  .banner-feature .brand-mark { width: 47px; height: 42px; }
  .banner-feature .brand-name { font-size: 14px; margin-left: 8px; letter-spacing: .07em; }
  .banner-feature .headline { left: 0; right: 0; top: 92px; font-size: 27px; }
  .banner-feature .subline { left: 60px; right: 60px; top: 147px; font-size: 20px; line-height: 1.45; }
  .banner-feature .act-now { left: 0; right: 0; top: 222px; font-size: 32px; }
  .banner-feature .check { left: 0; right: 0; top: 268px; font-size: 19.5px; }
  .banner-feature .cta { left: 206px; top: 313px; width: 222px; height: 37px; font-size: 10.5px; }
  .banner-feature .photo-band { position: absolute; left: 0; top: 370px; }
</style>
</head>
<body>
  <svg class="board-shapes" width="1200" height="1179" viewBox="0 0 1200 1179" aria-hidden="true">
    <defs>
      <linearGradient id="boardGlow" x1="0" y1="0" x2="0" y2="1">
        <stop offset="0" stop-color="#c9c9c9"/>
        <stop offset="1" stop-color="#bdbdbd"/>
      </linearGradient>
    </defs>
    <rect width="1200" height="1179" fill="url(#boardGlow)"/>
    <path d="M0 0 H235 Q150 110 0 226 Z" fill="var(--orange)"/>
    <path d="M1200 358 C880 480 640 760 660 1179 H1200 Z" fill="var(--navy)"/>
    <path d="M1200 892 C1100 970 1010 1060 968 1179 H1200 Z" fill="var(--orange)"/>
  </svg>

  <section class="banner banner-wide">
    <svg class="photo-ring" width="706" height="369" viewBox="0 0 706 369">
      <defs>
        <radialGradient id="wideScene" cx=".45" cy=".4" r=".7">
          <stop offset="0" stop-color="#d8c6ae"/>
          <stop offset=".6" stop-color="var(--photo-warm)"/>
          <stop offset="1" stop-color="#8f8a8c"/>
        </radialGradient>
      </defs>
      <rect x="313" y="102" width="20" height="15" rx="7.5" fill="var(--ring)"/>
      <rect x="343" y="102" width="60" height="15" rx="7.5" fill="var(--ring)"/>
      <rect x="356" y="126" width="47" height="15" rx="7.5" fill="var(--ring)"/>
      <circle cx="530" cy="184" r="160" fill="var(--ring)"/>
      <circle cx="530" cy="184" r="143" fill="var(--navy)"/>
      <circle cx="530" cy="184" r="134" fill="url(#wideScene)" role="img" aria-label="Photo: a woman helping a young man use a laptop at home"/>
    </svg>
    <div class="brand-row"><span class="brand-mark"></span><span class="brand-name">Free Social Security Disability Claim Evaluation</span></div>
    <h1 class="headline">Are you out of work<br>due to a disability?</h1>
    <p class="subline">You may qualify for up to $2,642<br>per month in Social Security<br>Disability benefits</p>
    <p class="act-now">ACT NOW</p>
    <p class="check">Check Your Eligibility Now</p>
    <a class="cta">Get Your Free Evaluation</a>
  </section>

  <section class="banner banner-square">
    <div class="photo-fill" role="img" aria-label="Background photo, tinted blue: a smiling older woman seated at home"></div>
    <div class="brand-row"><span class="brand-mark"></span><span class="brand-name">Free Social Security Disability Claim Evaluation</span></div>
    <h2 class="headline">Are you out of work<br>&nbsp;due to a disability?</h2>
    <p class="subline">You may qualify for up to $2,642 per month in<br>Social Security&nbsp; Disability benefits</p>
    <p class="act-now">ACT NOW</p>
    <p class="check">Check Your Eligibility Now</p>
    <a class="cta">Fast, Free, No Obligation Evaluation</a>
  </section>

  <section class="banner banner-feature">
    <div class="brand-row"><span class="brand-mark"></span><span class="brand-name">Free Social Security Disability Claim Evaluation</span></div>
    <h2 class="headline">Are you out of work due to a disability?</h2>
    <p class="subline">You may qualify for up to $2,642 per month in Social Security&nbsp; Disability benefits</p>
    <p class="act-now">ACT NOW</p>
    <p class="check">Check Your Eligibility Now</p>
    <a class="cta">Confirm My Eligibility Now!</a>
    <svg class="photo-band" width="635" height="265" viewBox="0 0 635 265">
      <defs>
        <linearGradient id="featureScene" x1="0" y1="0" x2="1" y2="0">
          <stop offset="0" stop-color="#d9d9d6"/>
          <stop offset=".45" stop-color="#c4b7aa"/>
          <stop offset="1" stop-color="var(--photo-cool)"/>
        </linearGradient>
      </defs>
      <path d="M0 54 Q317 -18 635 56 V265 H0 Z" fill="var(--white)"/>
      <path d="M0 66 Q317 -6 635 66 V265 H0 Z" fill="url(#featureScene)" role="img" aria-label="Photo: a young caregiver smiling with an older woman"/>
    </svg>
  </section>
</body>
</html>
```